Investment company seeks website design

KRV (Halvorsen Capital Partners) are an investment company that actively targets and acquires businesses and grows them after acquisition.

The website design needs to be professional and should communicate to key decision-makers inside the acquirable companies that KRV targets.

You will design the Homepage initially for the competition. If you win the competition, you will design the inner pages too.

More details are attached below.

Target Market(s)

Business owners and decision makers inside acquirable companies

Industry/Entity Type

Company Investment

Number of Pages Required

5+ page

Requirements
Must have
• High Attention to Detail. Following the Wireframes closely. Consistent colour and design choices
Should not have
• Anything cheap, too bright or untidy

```html
<!DOCTYPE html>
<html lang="en">
<head>
<meta charset="utf-8">
<title>KRV — Halvorsen Capital Partners</title>
<link href="https://fonts.googleapis.com/css2?family=Poppins:wght@400;500;600;700;800&display=swap" rel="stylesheet">
<style>
:root{
  --navy:#1f3162;
  --navy-deep:#182850;
  --green:#6ab23e;
  --green-soft:#e4efd8;
  --ink:#222a36;
  --muted:#4a5160;
  --paper:#ffffff;
  --grey:#f3f4f5;
}
*{box-sizing:border-box;margin:0;padding:0}
html,body{width:1200px;height:5038px;overflow:hidden}
body{font-family:'Poppins',sans-serif;color:var(--ink);background:var(--paper);position:relative}
.abs{position:absolute}
.btn{position:absolute;background:var(--green);color:#fff;font-weight:700;font-size:11px;letter-spacing:.3px;border-radius:22px;display:flex;align-items:center;justify-content:center;text-transform:uppercase}
h2{font-weight:800;text-transform:uppercase;line-height:1.15}

/* header */
.site-header{position:absolute;top:0;left:0;width:1200px;height:82px;background:#fff}
.brand{position:absolute;display:flex;align-items:center;gap:12px}
.brand-mark{width:40px;height:40px;background:var(--navy);border-radius:4px}
.brand-name{font-weight:500;font-size:21px;color:var(--navy);letter-spacing:.5px;line-height:1}
.nav{position:absolute;left:485px;top:32px;display:flex;gap:30px;font-size:11px;font-weight:600;color:var(--navy)}

/* hero */
.hero{position:absolute;top:82px;left:0;width:1200px;height:608px;overflow:hidden}
.hero-left{position:absolute;inset:0;background:
  radial-gradient(circle at 150px 120px,rgba(120,140,190,.45),transparent 220px),
  radial-gradient(ellipse at 330px 460px,rgba(10,20,50,.55),transparent 300px),
  linear-gradient(135deg,#2d4378,#14234a)}
.hero-right{position:absolute;inset:0;background:
  radial-gradient(circle at 820px 180px,rgba(170,220,120,.55),transparent 230px),
  radial-gradient(ellipse at 1000px 470px,rgba(40,90,20,.5),transparent 300px),
  linear-gradient(135deg,#83c452,#4c8c28);clip-path:polygon(565px 0,1200px 0,1200px 608px,485px 608px)}
.hero-title{position:absolute;color:#fff;font-weight:800;font-size:40px;line-height:1.2;text-transform:uppercase}
.hero-badge{position:absolute;left:526px;top:325px;width:80px;height:80px;border-radius:50%;background:#fff;border:4px solid #e9ecef;display:flex;align-items:center;justify-content:center;font-weight:800;font-size:18px;color:var(--navy)}

/* thrive */
.thrive-photo{position:absolute;left:130px;top:778px;width:500px;height:508px;border-radius:120px 0 0 0;background:
  radial-gradient(ellipse at 260px 180px,#f0d9c4,transparent 150px),
  radial-gradient(ellipse at 250px 420px,#efe9e2,transparent 200px),
  linear-gradient(160deg,#caa98a,#6f5440)}
.thrive-frame{position:absolute;left:150px;top:776px;width:480px;height:490px;border:7px solid var(--green);border-radius:120px 0 0 0;border-left:none;border-bottom:none}
.dots{position:absolute;background-image:radial-gradient(#c9ced6 1.4px,transparent 1.6px);background-size:14px 14px}
.thrive-copy{position:absolute;left:705px;top:798px;width:420px}
.thrive-copy h2{font-size:34px;color:var(--ink)}
.thrive-copy p{font-size:13px;line-height:1.75;color:var(--muted);margin-top:14px}
.services-title{font-size:12px;font-weight:700;margin-top:20px}
.tick-list{list-style:none;margin-top:10px}
.tick-list li{font-size:12.5px;color:var(--muted);display:flex;align-items:center;gap:10px;line-height:23px}
.tick{width:13px;height:13px;border-radius:50%;background:var(--green);flex:none;position:relative}
.tick::after{content:"";position:absolute;left:3.5px;top:3.5px;width:4px;height:4px;border-right:1.6px solid #fff;border-top:1.6px solid #fff;transform:rotate(45deg)}

/* qualities */
.qualities{position:absolute;top:1368px;left:0;width:1200px;height:690px;background:var(--navy)}
.qualities h2{position:absolute;top:70px;width:100%;text-align:center;color:#fff;font-size:32px}
.q-grid{position:absolute;left:130px;top:156px;width:938px;height:438px;display:grid;grid-template-columns:1fr 1fr;grid-template-rows:1fr 1fr}
.q-cell{position:relative;padding:58px 44px 0}
.q-cell h3{font-size:15.5px;font-weight:700;text-transform:uppercase;line-height:1.5}
.q-cell ul{list-style:none;margin-top:10px}
.q-cell li{font-size:12.5px;color:var(--muted);display:flex;gap:10px;line-height:23px}
.q-cell li .tick{margin-top:5px}
.q-cell.right{text-align:right}
.q-cell.right li{justify-content:flex-end}
.q-white{background:#fff}.q-green{background:var(--green-soft)}
.q-icon{position:absolute;width:76px;height:76px}
.q-center{position:absolute;left:519px;top:1670px;width:158px;height:158px;border-radius:50%;background:var(--navy);border:6px solid var(--green);display:flex;align-items:center;justify-content:center;color:#fff;font-weight:800;font-size:34px;letter-spacing:1px}

/* explore */
.explore-photo{position:absolute;top:2250px;left:0;width:1200px;height:486px;background:
  radial-gradient(ellipse at 760px 250px,rgba(255,255,255,.7),transparent 120px),
  radial-gradient(ellipse at 300px 420px,rgba(90,110,150,.45),transparent 260px),
  radial-gradient(ellipse at 1000px 420px,rgba(120,95,75,.45),transparent 260px),
  linear-gradient(180deg,#ffffff 0%,#e2dbd3 30%,#a99a8c 100%)}
.explore-frame{position:absolute;left:250px;top:2166px;width:700px;height:130px;border:2px solid var(--navy);border-top:none}
.explore-frame::before,.explore-frame::after{content:"";position:absolute;top:0;height:2px;width:60px;background:var(--navy)}
.explore-frame::before{left:0}.explore-frame::after{right:0}
.explore-title{position:absolute;top:2140px;width:1200px;text-align:center;color:var(--navy);font-size:42px}
.explore-text{position:absolute;top:2200px;width:1200px;text-align:center;font-size:13.5px;line-height:1.8;color:var(--ink)}

/* transform */
.transform{position:absolute;top:2736px;left:0;width:1200px;height:598px;background:var(--grey)}
.transform h2{position:absolute;top:70px;width:100%;text-align:center;font-size:33px;color:var(--ink)}
.step{position:absolute;width:260px;text-align:center}
.step h3{font-size:15.5px;font-weight:700;text-transform:uppercase;line-height:1.5}
.step p{font-size:12.5px;color:var(--muted);line-height:1.65;margin-top:8px}

/* news */
.news{position:absolute;top:3334px;left:0;width:1200px;height:676px;background:var(--navy)}
.news h2{position:absolute;top:64px;width:100%;text-align:center;color:#fff;font-size:32px}
.card{position:absolute;top:140px;width:292px;color:#fff}
.card-img{height:230px;border-radius:3px}
.card-date{color:var(--green);font-size:12.5px;margin-top:22px}
.card h3{font-size:12.5px;font-weight:700;line-height:1.55;margin-top:4px;text-transform:uppercase}
.card p{font-size:11.5px;line-height:1.6;margin-top:8px;color:#e3e7f0}

/* balance */
.balance h2{position:absolute;top:4086px;width:1200px;text-align:center;font-size:33px;color:var(--ink)}
.pillar{position:absolute;width:140px;text-align:center;font-size:14px;font-weight:700;text-transform:uppercase}
.pillar-icon{width:62px;height:62px;border-radius:50%;background:var(--navy);margin:0 auto 14px;border:3px solid #dfe4ee;display:flex;align-items:center;justify-content:center}
.balance-core{position:absolute;left:490px;top:4340px;width:220px;height:220px;border-radius:50%;background:var(--navy);border:8px solid var(--green);display:flex;align-items:center;justify-content:center;color:#fff;font-weight:800;font-size:48px;letter-spacing:2px}

/* footer */
.site-footer{position:absolute;top:4674px;left:0;width:1200px;height:364px;background:var(--navy);color:#fff}
.social{position:absolute;left:130px;top:139px;display:flex;gap:10px}
.social span{width:36px;height:36px;border-radius:50%;border:1.5px solid #fff}
.f-links{position:absolute;left:395px;top:62px;font-size:11.5px;line-height:22px}
.f-head{font-size:12px;font-weight:700;text-transform:uppercase}
.f-round{width:30px;height:30px;border-radius:50%;background:var(--green);flex:none;display:flex;align-items:center;justify-content:center}
.f-block{position:absolute;display:flex;gap:14px;font-size:11.5px;line-height:21px}
.f-rule{position:absolute;left:130px;top:292px;width:940px;height:1px;background:#3c4d7b}
.f-bottom{position:absolute;top:306px;font-size:12.5px}
</style>
</head>
<body>

<header class="site-header">
  <div class="brand" style="left:55px;top:20px">
    <span class="brand-mark"></span>
    <span class="brand-name">HALVORSEN</span>
  </div>
  <nav class="nav"><span>OUR APPROACH</span><span>INVESTMENT CRITERIA</span><span>ABOUT US</span><span>CONTACT US</span></nav>
  <div class="btn" style="left:1000px;top:23px;width:137px;height:36px">Email us</div>
</header>

<section class="hero">
  <div class="hero-left" role="img" aria-label="Photo of professionals working at laptops in an office, navy tint"></div>
  <div class="hero-right" role="img" aria-label="Photo of smiling colleagues reviewing a tablet together, green tint"></div>
  <div class="hero-title" style="left:130px;top:192px">The best exit<br>for you</div>
  <div class="btn" style="left:130px;top:306px;width:170px;height:40px">Discover KRV</div>
  <div class="hero-title" style="left:735px;top:200px">The best<br>future for<br>your business</div>
  <div class="hero-badge">KRV</div>
</section>

<section class="thrive">
  <div class="dots" style="left:95px;top:1160px;width:160px;height:160px"></div>
  <div class="dots" style="left:560px;top:770px;width:80px;height:80px"></div>
  <div class="thrive-photo" role="img" aria-label="Photo of a smiling businesswoman holding a tablet"></div>
  <div class="thrive-frame"></div>
  <div class="thrive-copy">
    <h2>We will make your<br>business thrive</h2>
    <p>KRV is committed to helping businesses achieve significant growth. Under our stewardship, companies have the benefit of an experienced team expert in operations and financing to ensure that every company achieves their full potential.</p>
    <div class="services-title">OUR SERVICES INCLUDE:</div>
    <ul class="tick-list">
      <li><span class="tick"></span>Crafting long-term growth</li>
      <li><span class="tick"></span>Streamlining operations for maximum efficiency</li>
      <li><span class="tick"></span>Providing expert advice to improve management decisions</li>
      <li><span class="tick"></span>Optimising financial structures for expansion</li>
      <li><span class="tick"></span>Facilitating strategic mergers and acquisitions</li>
    </ul>
  </div>
  <div class="btn" style="left:705px;top:1193px;width:224px;height:38px">Unlock your potential</div>
</section>

<section class="qualities">
  <h2>Our qualities &amp; capabilities</h2>
  <div class="q-grid">
    <div class="q-cell q-white">
      <h3>Driving value</h3>
      <ul>
        <li><span class="tick"></span>Comprehensive long-term plan</li>
        <li><span class="tick"></span>Ownership of company performance</li>
        <li><span class="tick"></span>Vast experience in driving transformation</li>
      </ul>
      <svg class="q-icon" style="left:350px;top:30px" viewBox="0 0 76 76" role="img" aria-label="Growth chart icon">
        <rect x="6" y="8" width="64" height="48" rx="4" fill="#fff" stroke="#1f3162" stroke-width="3"/>
        <g fill="#6ab23e"><rect x="38" y="36" width="6" height="14"/><rect x="48" y="28" width="6" height="22"/><rect x="58" y="20" width="6" height="30"/></g>
        <circle cx="22" cy="28" r="10" fill="none" stroke="#1f3162" stroke-width="3"/>
        <path d="M22 22v12M19 25h6M19 31h6" stroke="#6ab23e" stroke-width="2.5"/>
        <path d="M28 56v10M48 56v10M20 66h36" stroke="#1f3162" stroke-width="3"/>
      </svg>
    </div>
    <div class="q-cell q-green right">
      <h3>Integrated team</h3>
      <ul>
        <li>Partnership Culture<span class="tick"></span></li>
        <li>Consistent senior team<span class="tick"></span></li>
        <li>Detailed industry and operating experience<span class="tick"></span></li>
      </ul>
      <svg class="q-icon" style="left:40px;top:30px" viewBox="0 0 76 76" role="img" aria-label="Team icon">
        <g fill="none" stroke="#1f3162" stroke-width="3">
          <circle cx="38" cy="30" r="8"/><path d="M24 62c0-12 6-18 14-18s14 6 14 18z"/>
          <circle cx="14" cy="36" r="6"/><path d="M4 62c0-9 4-14 10-14"/>
          <circle cx="62" cy="36" r="6"/><path d="M72 62c0-9-4-14-10-14"/>
        </g>
        <path d="M38 6v10M33 11l5-5 5 5M14 12v12M62 12v12" stroke="#6ab23e" stroke-width="3" fill="none"/>
      </svg>
    </div>
    <div class="q-cell q-green">
      <h3>Partnership with<br>management</h3>
      <ul>
        <li><span class="tick"></span>Strong, trust-based relationships</li>
        <li><span class="tick"></span>Significant commitment of time<br>on-the-ground</li>
        <li><span class="tick"></span>Ability to take interim roles if needed</li>
      </ul>
      <svg class="q-icon" style="left:350px;top:120px" viewBox="0 0 76 76" role="img" aria-label="Target and handshake icon">
        <circle cx="38" cy="18" r="12" fill="none" stroke="#6ab23e" stroke-width="3"/>
        <circle cx="38" cy="18" r="4" fill="#1f3162"/>
        <g fill="none" stroke="#1f3162" stroke-width="3" stroke-linejoin="round">
          <path d="M4 48l12-10 10 4 12-6 10 6 12-4 12 10"/>
          <path d="M26 42l14 16c3 3 7 0 4-4M34 50l8 8M44 46l8 8"/>
        </g>
      </svg>
    </div>
    <div class="q-cell q-white right">
      <h3 style="margin-top:12px">Accelerated execution</h3>
      <ul>
        <li>Relentless focus on priorities<span class="tick"></span></li>
        <li>Drive through to results<span class="tick"></span></li>
        <li>Committed to continuous development<span class="tick"></span></li>
      </ul>
      <svg class="q-icon" style="left:40px;top:120px" viewBox="0 0 76 76" role="img" aria-label="Clock and briefcase icon">
        <circle cx="30" cy="32" r="22" fill="#e4efd8" stroke="#1f3162" stroke-width="3"/>
        <path d="M30 18v14l9 6" stroke="#6ab23e" stroke-width="3" fill="none" stroke-linecap="round"/>
        <rect x="40" y="46" width="30" height="22" rx="3" fill="#fff" stroke="#1f3162" stroke-width="3"/>
        <path d="M49 46v-5h12v5M40 56h30" stroke="#1f3162" stroke-width="3" fill="none"/>
      </svg>
    </div>
  </div>
</section>
<div class="q-center">KRV</div>

<section class="explore">
  <div class="explore-photo" role="img" aria-label="Photo of a presenter speaking to a seated group of young professionals"></div>
  <div class="explore-frame"></div>
  <h2 class="explore-title">Explore your next move</h2>
  <p class="explore-text">If you are looking for a change, then KRV can help you map out a smooth transition,<br>and give you the confidence that your company is in safe hands.</p>
  <div class="btn" style="left:515px;top:2275px;width:170px;height:38px">Discuss with KRV</div>
</section>

<section class="transform">
  <h2>How KRV will transform<br>your company</h2>
  <svg class="abs" style="left:0;top:0" width="1200" height="400" aria-hidden="true">
    <g fill="none" stroke="#9cca7b" stroke-width="2">
      <line x1="345" y1="286" x2="513" y2="286"/>
      <line x1="693" y1="286" x2="865" y2="286"/>
    </g>
    <g fill="none" stroke="#6ab23e" stroke-width="5" stroke-linecap="round">
      <path d="M165 286 A90 90 0 0 1 255 196"/>
      <path d="M513 286 A90 90 0 0 1 603 196"/>
      <path d="M955 196 A90 90 0 0 1 1045 286"/>
    </g>
    <g fill="#1f3162">
      <circle cx="255" cy="286" r="80"/>
      <circle cx="603" cy="286" r="80"/>
      <circle cx="955" cy="286" r="80"/>
    </g>
    <g fill="none" stroke="#fff" stroke-width="3" stroke-linecap="round" stroke-linejoin="round">
      <circle cx="255" cy="286" r="30" stroke-dasharray="8 5"/>
      <circle cx="255" cy="286" r="20"/>
      <path d="M237 300l12-12 8 8 20-20M267 276h10v10"/>
      <circle cx="585" cy="268" r="7"/><circle cx="621" cy="268" r="7"/>
      <path d="M572 300c0-12 6-18 13-18s13 6 13 18M608 300c0-12 6-18 13-18s13 6 13 18"/>
      <path d="M576 300h54M590 300v12M616 300v12"/>
      <rect x="592" y="244" width="22" height="14" rx="3"/>
      <path d="M930 304l18-18 10 8 14-14 16 16"/>
      <path d="M946 258l-6-8M955 254v-10M964 258l6-8"/>
      <path d="M930 304l10 10 14-4 20-20"/>
    </g>
  </svg>
  <div class="step" style="left:125px;top:398px"><h3>Discover growth<br>opportunities</h3><p>Identify hidden growth<br>opportunities for your business</p></div>
  <div class="step" style="left:473px;top:398px"><h3>Craft strategic<br>solutions</h3><p>Develop precise, results-driven<br>strategies to drive your company<br>forward</p></div>
  <div class="step" style="left:825px;top:398px"><h3>Drive future<br>success</h3><p>Lead your company through<br>transformative processes to<br>achieve tangible success</p></div>
</section>

<section class="news">
  <h2>KRV news &amp; insights</h2>
  <article class="card" style="left:130px">
    <div class="card-img" role="img" aria-label="Photo of a woman presenting to colleagues in a meeting room" style="background:radial-gradient(ellipse at 200px 110px,#8a6a5a,transparent 90px),radial-gradient(ellipse at 70px 60px,#f2f5f8,transparent 110px),linear-gradient(135deg,#c9d3dc,#56687c)"></div>
    <div class="card-date">5 Feb 2024</div>
    <h3>Praesent convallis sem non velit hendrerit, sit amet cursus</h3>
    <p>Lorem ipsum dolor sit amet, consectetur adipiscing elit, sed do eiusmod tempor incididunt ut labore et dolore magna aliqua. Ut enim ad minim veniam, quis nostrud</p>
  </article>
  <article class="card" style="left:455px">
    <div class="card-img" role="img" aria-label="Photo of a business team meeting around a table" style="background:radial-gradient(ellipse at 150px 150px,#2c3550,transparent 120px),radial-gradient(ellipse at 150px 40px,#f5f6f7,transparent 130px),linear-gradient(135deg,#d6dbe0,#5e6b7c)"></div>
    <div class="card-date">5 Feb 2024</div>
    <h3>Praesent convallis sem non velit hendrerit, sit amet cursus</h3>
    <p>Lorem ipsum dolor sit amet, consectetur adipiscing elit, sed do eiusmod tempor incididunt ut labore et dolore magna aliqua. Ut enim ad minim veniam, quis nostrud</p>
  </article>
  <article class="card" style="left:780px">
    <div class="card-img" role="img" aria-label="Photo of an analyst reviewing charts on a laptop" style="background:radial-gradient(ellipse at 230px 110px,#2e3748,transparent 110px),radial-gradient(ellipse at 60px 110px,#dfe8f3,transparent 100px),linear-gradient(135deg,#e2e6ea,#7c8794)"></div>
    <div class="card-date">5 Feb 2024</div>
    <h3>Praesent convallis sem non velit hendrerit, sit amet cursus</h3>
    <p>Lorem ipsum dolor sit amet, consectetur adipiscing elit, sed do eiusmod tempor incididunt ut labore et dolore magna aliqua. Ut enim ad minim veniam, quis nostrud</p>
  </article>
  <div class="btn" style="left:482px;top:572px;width:236px;height:38px">View all KRV news &amp; insights</div>
</section>

<section class="balance">
  <h2>Halvorsen Capital Partners<br>Group: providing balance and<br>growth to your business</h2>
  <svg class="abs" style="left:0;top:4250px" width="1200" height="350" aria-hidden="true">
    <g fill="none" stroke="#222a36" stroke-width="2" stroke-linecap="round">
      <path d="M505 100 C495 70 475 60 455 68"/><path d="M455 68 l8 -6 M455 68 l9 4"/>
      <path d="M695 100 C705 70 725 60 745 68"/><path d="M745 68 l-8 -6 M745 68 l-9 4"/>
      <path d="M530 290 C525 320 510 330 495 328"/><path d="M495 328 l8 -6 M495 328 l8 5"/>
      <path d="M660 290 C665 320 680 330 695 328"/><path d="M695 328 l-8 -6 M695 328 l-8 5"/>
    </g>
  </svg>
  <div class="balance-core">KRV</div>
  <div class="pillar" style="left:310px;top:4280px"><div class="pillar-icon" role="img" aria-label="Finance icon"><svg width="30" height="30" viewBox="0 0 30 30" fill="none" stroke="#fff" stroke-width="2.2"><rect x="5" y="3" width="18" height="24" rx="2"/><path d="M9 9h10M9 14h10M9 19h5"/><circle cx="22" cy="22" r="5" fill="#1f3162"/></svg></div>Finance</div>
  <div class="pillar" style="left:742px;top:4278px"><div class="pillar-icon" role="img" aria-label="Strategy icon"><svg width="30" height="30" viewBox="0 0 30 30" fill="none" stroke="#fff" stroke-width="2.2"><rect x="3" y="5" width="24" height="16" rx="2"/><path d="M7 17l5-5 4 3 7-7M10 25h10"/></svg></div>Strategy</div>
  <div class="pillar" style="left:340px;top:4476px"><div class="pillar-icon" role="img" aria-label="Partnerships icon"><svg width="30" height="30" viewBox="0 0 30 30" fill="none" stroke="#fff" stroke-width="2.2"><circle cx="9" cy="9" r="4"/><circle cx="21" cy="9" r="4"/><path d="M2 25c0-6 3-9 7-9s7 3 7 9M14 25c0-6 3-9 7-9s7 3 7 9"/></svg></div>Partnerships</div>
  <div class="pillar" style="left:702px;top:4476px"><div class="pillar-icon" role="img" aria-label="Operations icon"><svg width="30" height="30" viewBox="0 0 30 30" fill="none" stroke="#fff" stroke-width="2.2"><circle cx="15" cy="15" r="5"/><path d="M15 3v4M15 23v4M3 15h4M23 15h4M6.5 6.5l3 3M20.5 20.5l3 3M6.5 23.5l3-3M20.5 9.5l3-3"/></svg></div>Operations</div>
</section>

<footer class="site-footer">
  <div class="brand" style="left:130px;top:66px">
    <span class="brand-mark" style="background:#fff"></span>
    <span class="brand-name" style="color:#fff">HALVORSEN</span>
  </div>
  <div class="social"><span></span><span></span><span></span></div>
  <div class="f-links">Our Approach<br>Investment Criteria<br>About Us<br>Contact Us</div>
  <div class="f-head abs" style="left:572px;top:62px">Our team</div>
  <div class="f-block" style="left:572px;top:94px">
    <span class="f-round"><svg width="14" height="14" viewBox="0 0 24 24"><path fill="#fff" d="M6.6 10.8a15 15 0 0 0 6.6 6.6l2.2-2.2c.3-.3.7-.4 1-.2 1.1.4 2.3.6 3.6.6.6 0 1 .4 1 1V20c0 .6-.4 1-1 1A17 17 0 0 1 3 4c0-.6.4-1 1-1h3.5c.6 0 1 .4 1 1 0 1.3.2 2.5.6 3.6.1.3 0 .7-.2 1z"/></svg></span>
    <div>CALL US<br>+44 (0) 7700 900123</div>
  </div>
  <div class="btn" style="left:575px;top:150px;width:158px;height:34px">Email</div>
  <div class="f-head abs" style="left:812px;top:62px">Address</div>
  <div class="f-block" style="left:812px;top:94px">
    <span class="f-round"><svg width="12" height="16" viewBox="0 0 12 16"><path fill="#fff" d="M6 0a6 6 0 0 0-6 6c0 4.5 6 10 6 10s6-5.5 6-10a6 6 0 0 0-6-6zm0 8.3A2.3 2.3 0 1 1 6 3.7a2.3 2.3 0 0 1 0 4.6z"/></svg></span>
    <div style="font-size:10.5px">HALVORSEN CAPITAL PARTNERS LTD.<br>12 HARBOUR COURT, MARLOW STREET<br>BRIDGETOWN<br>BARBADOS</div>
  </div>
  <div class="f-rule"></div>
  <div class="f-bottom" style="left:130px">© 2024 Halvorsen Capital Partners Ltd. All rights reserved.</div>
  <div class="f-bottom" style="left:685px;width:385px;text-align:right">Sitemap &nbsp;|&nbsp; Terms of Use &nbsp;|&nbsp; Privacy Policy &nbsp;|&nbsp; Contact Us</div>
</footer>

</body>
</html>
```